Business Card Design Project - KLB

I am looking for a more sophisticated card design for my company,
"The Kestrel Bureau"

We are a consultancy focused on strategy and change in Associations and professional organisations.

I am a lawyer and psychologist with a PhD and so am looking for something that communicates seriousness and credibility but also quirky creative solutions for strategic problems, which is my field of speciality.

I am looking for something that is quietly spoken, rather than loud colours ('credible' and 'creative' are the two adjectives that I think of as competing here).

I particularly like an embossed card style - heavy white card with plain white or white and black or white and grey text.

The key logo image for the company is a question mark and I am open to suggestions and ideas on design.

I have attached a file that includes a couple of styles that have caught my eye and my thoughts on them. Hopefully they communicate what I'm looking for.
Updates

Thank you for all the great suggestions and designs.

I really appreciated the effort and creative energy you put into your designs. I have now closed the project after selecting a design and advising the successful designer of the card that I am happy with.

Regards

Target Market(s)

Organisations (CEO's and Boards), Governments, Legal professionals, Membership Associations and aspiring professionals.

Industry/Entity Type

Lawyer

Requirements
Must have
• The key logo element is a question mark (?) and this needs to be incorporated.

Embossed style - cut outs or other design ideas interest me too.

The attached file has a number of sample ideas and comments on each one that I like.
Should not have
• I like crisp, modern fonts (Myriads etc...) and do not like embellished fonts or Times etc...

```html
<!DOCTYPE html>
<html lang="en">
<head>
<meta charset="utf-8">
<title>The Kestrel Bureau – Business Card</title>
<link rel="stylesheet" href="https://fonts.googleapis.com/css2?family=Crimson+Pro:ital,wght@0,400;0,600;1,700&family=Roboto+Condensed:wght@400;500&family=Zilla+Slab:wght@400&display=swap">
<style>
  :root {
    --ink: #000000;
    --paper: #ffffff;
    --accent: #e8161b;
    --mark-area: #2b2b2b;
  }
  html, body {
    margin: 0;
    padding: 0;
    width: 1200px;
    height: 686px;
    overflow: hidden;
    background: var(--paper);
  }
  .card {
    position: relative;
    width: 1200px;
    height: 686px;
    background: var(--paper);
    overflow: hidden;
  }
  .brand-panel {
    position: absolute;
    left: 0;
    top: 0;
    width: 535px;
    height: 686px;
    background: var(--ink);
  }
  .brand-mark {
    position: absolute;
    left: 88px;
    top: 100px;
    width: 340px;
    height: 340px;
    background: var(--mark-area);
  }
  .brand-name {
    position: absolute;
    left: 34px;
    top: 566px;
    margin: 0;
    font-family: "Zilla Slab", Georgia, serif;
    font-weight: 400;
    font-size: 72px;
    line-height: 1;
    color: var(--paper);
    white-space: nowrap;
  }
  .divider {
    position: absolute;
    left: 544px;
    top: 0;
    width: 9px;
    height: 686px;
    background: var(--ink);
  }
  .details {
    position: absolute;
    left: 574px;
    top: 0;
    right: 0;
    height: 686px;
    font-family: "Crimson Pro", Georgia, serif;
    color: var(--ink);
  }
  .details > * {
    position: absolute;
    left: 0;
    margin: 0;
    line-height: 1;
    white-space: nowrap;
  }
  .person-name {
    top: 290px;
    font-size: 48px;
    font-weight: 400;
  }
  .person-role {
    left: 4px;
    top: 343px;
    font-family: "Roboto Condensed", "Arial Narrow", sans-serif;
    font-size: 34px;
    font-weight: 500;
    color: var(--accent);
  }
  .company {
    top: 410px;
    font-size: 33px;
    font-style: italic;
    font-weight: 700;
  }
  .contact {
    font-size: 22px;
    font-weight: 600;
  }
  .contact .label { color: var(--accent); margin-right: 6px; }
  .contact-mobile { top: 468px; }
  .contact-phone  { top: 519px; }
  .contact-email  { top: 571px; }
  .contact-post   { top: 620px; }
</style>
</head>
<body>
  <main class="card">
    <section class="brand-panel">
      <div class="brand-mark" role="img" aria-label="Place for the company question-mark logo mark"></div>
      <p class="brand-name">kestrel bureau</p>
    </section>
    <div class="divider"></div>
    <section class="details">
      <h1 class="person-name">Dr. Maren Holt</h1>
      <p class="person-role">Director</p>
      <p class="company">The Kestrel Bureau</p>
      <p class="contact contact-mobile"><span class="label">M:::</span> +61400 271 904</p>
      <p class="contact contact-phone"><span class="label">P:::</span>&nbsp; +612 9000 4417</p>
      <p class="contact contact-email"><span class="label">E:::</span> maren@kestrelbureau.com.au</p>
      <p class="contact contact-post"><span class="label">PO:::</span> P.O. Box 4181, Harlow Vale, Sydney, Australia</p>
    </section>
  </main>
</body>
</html>
```